Simple AD for Digital Publication

Total Size 5" x 5", may include boarder or not
Image Provided; crop or use as background
Incorporate Logo and text as provided

Target Market(s)

Sound Contractors / Integrators

Industry/Entity Type

Audio Video Lighting

Requirements
Must have
• Bold Look that reflects our brand. see website: tovermundic.com - cohesive text and style

```html
<!DOCTYPE html>
<html lang="en">
<head>
<meta charset="utf-8">
<title>Become a Dealer – Tovermundic Stage Co</title>
<link rel="stylesheet" href="https://fonts.googleapis.com/css2?family=Lilita+One&family=Montserrat:wght@800&family=Oswald:wght@600&family=Roboto:wght@500&display=swap">
<style>
  :root {
    --page-bg: #ececec;
    --banner-top: #b3202a;
    --banner-bottom: #f26a22;
    --frame-red: #e8202c;
    --white: #ffffff;
    --ink: #231f20;
    --brand-red: #b5121b;
    --shield-teal: #2fb5bf;
    --shield-deep: #17818e;
  }
  * { margin: 0; padding: 0; box-sizing: border-box; }
  html, body { width: 774px; height: 1200px; overflow: hidden; background: var(--page-bg); }
  .canvas { position: relative; width: 774px; height: 1200px; }
  .ad {
    position: absolute; left: 0; top: 213px; width: 774px; height: 774px; overflow: hidden;
    box-shadow: 0 6px 18px rgba(0,0,0,.35);
  }
  .ad-photo {
    position: absolute; inset: 0;
    background:
      radial-gradient(ellipse 45% 30% at 45% 30%, rgba(60,90,40,.75), transparent 70%),
      radial-gradient(ellipse 35% 25% at 80% 42%, rgba(200,110,70,.55), transparent 70%),
      radial-gradient(ellipse 55% 22% at 52% 70%, #3a2418, transparent 75%),
      linear-gradient(180deg, #120d0c 0%, #2a2417 30%, #4a3328 52%, #6e5466 72%, #6b5470 100%);
  }
  .dealer-banner {
    position: absolute; left: 51px; top: 0; width: 656px; height: 74px;
    border-radius: 0 0 10px 10px;
    background: linear-gradient(180deg, var(--banner-top), var(--banner-bottom));
    display: flex; align-items: center; justify-content: center;
    font-family: "Montserrat", sans-serif; font-weight: 800; font-size: 35px;
    color: var(--white); letter-spacing: -0.5px; white-space: pre;
  }
  .overlay { position: absolute; inset: 0; }
  .headline {
    position: absolute; left: 215px; top: 172px; width: 330px;
    font-family: "Lilita One", sans-serif; font-size: 39px; line-height: 39px;
    color: var(--white); text-transform: uppercase; text-align: center;
    letter-spacing: 0.5px; text-shadow: 0 2px 6px rgba(0,0,0,.5);
    transform: translateX(0); white-space: nowrap;
  }
  .headline span { display: block; margin-left: -40px; margin-right: -40px; }
  .brand-bar {
    position: absolute; left: 0; top: 630px; width: 462px; height: 73px;
    background: var(--white); border-radius: 0 40px 40px 0;
    display: flex; align-items: center; padding-left: 34px; gap: 16px;
  }
  .brand-mark { width: 40px; height: 40px; background: var(--brand-red); flex: none; }
  .brand-text { display: flex; flex-direction: column; }
  .brand-name {
    font-family: "Oswald", sans-serif; font-weight: 600; font-size: 30px; line-height: 32px;
    color: var(--ink); text-transform: uppercase;
  }
  .brand-tagline {
    font-family: "Roboto", sans-serif; font-weight: 500; font-size: 14px; line-height: 16px;
    color: var(--ink);
  }
</style>
</head>
<body>
<main class="canvas">
  <section class="ad">
    <div class="ad-photo" role="img" aria-label="Close-up photo of a stage floor pocket with cables running out, blurred stage lights and greenery behind"></div>

    <svg class="overlay" width="774" height="774" viewBox="0 0 774 774" aria-hidden="true">
      <defs>
        <linearGradient id="shield-fill" x1="0" y1="0" x2="0" y2="1">
          <stop offset="0" stop-color="var(--shield-teal)"/>
          <stop offset="1" stop-color="var(--shield-deep)"/>
        </linearGradient>
      </defs>
      <polyline class="frame" points="119,522 77,141 627,136 625,427"
        fill="none" stroke="var(--frame-red)" stroke-width="10" stroke-linejoin="round" stroke-linecap="round"/>
      <circle cx="364" cy="390" r="136" fill="rgba(255,255,255,.06)" stroke="rgba(255,255,255,.12)"/>
      <circle cx="364" cy="390" r="95" fill="rgba(255,255,255,.08)" stroke="rgba(255,255,255,.15)"/>
      <path class="shield" d="M364,318 C390,330 408,332 422,330 C426,380 412,425 364,452 C316,425 302,380 306,330 C320,332 338,330 364,318 Z"
        fill="url(#shield-fill)" stroke="#d9e4e8" stroke-width="5"/>
      <circle cx="364" cy="380" r="22" fill="var(--white)"/>
      <polyline points="353,381 361,389 376,373" fill="none" stroke="var(--shield-deep)" stroke-width="6" stroke-linecap="round" stroke-linejoin="round"/>
    </svg>

    <div class="dealer-banner">BECOME A DEALER  (CLICK HERE)</div>

    <h1 class="headline">
      <span>Protect and Conceal</span>
      <span>High and Low</span>
      <span>Voltage Connectivity</span>
    </h1>

    <div class="brand-bar">
      <div class="brand-mark"></div>
      <div class="brand-text">
        <span class="brand-name">Tovermundic Stage Co</span>
        <span class="brand-tagline">Stage Pocket Systems Connectivity</span>
      </div>
    </div>
  </section>
</main>
</body>
</html>
```